A restaurant needs a new design for menu and presentation flyers.

The name of the restaurant located in Germany is ,, GASTSTÄTTE ZUM MÜHLSTEG" . It means RESTAURANT THE MILL BRIDGE. I attached two photos for reference to see the actual fonts.
I would like to have something close to the fonts we have now. I would like to add a crown representation.Any idea is welcomed.

Target Market(s)

GERMANY

Contact Information for Business Card

Must have ZUM MÜHLSTEG logo.

Requirements
Nice to have
• A crown representation or other symbol who can be representative for our business.
An font close to actual fonts.

```html
<!DOCTYPE html>
<html lang="de">
<head>
<meta charset="utf-8">
<title>Gaststätte Zum Mühlsteg – Menu</title>
<link rel="stylesheet" href="https://fonts.googleapis.com/css2?family=Barlow:wght@400;500&family=Barlow+Condensed:wght@400;600&family=Great+Vibes&display=swap">
<style>
  :root{
    --cream:#fdeedb;
    --gold:#c98935;
    --gold-light:#e2b265;
    --ink:#1e1612;
    --muted:#8b7c70;
    --dark-1:#2a0a03;
    --dark-2:#5a1806;
    --dark-3:#7a4a16;
  }
  *{margin:0;padding:0;box-sizing:border-box}
  html,body{width:1200px;height:856px;overflow:hidden;background:var(--cream)}
  .menu-sheet{position:relative;width:1200px;height:856px;background:var(--cream);font-family:"Barlow",sans-serif;color:var(--ink)}

  /* left brand panel */
  .brand-panel{position:absolute;left:0;top:0;width:404px;height:856px;
    background:
      radial-gradient(circle at 270px 590px, rgba(150,95,30,.55) 0, rgba(150,95,30,0) 70px),
      radial-gradient(circle at 30px 640px, rgba(140,85,25,.5) 0, rgba(140,85,25,0) 70px),
      radial-gradient(circle at 220px 240px, rgba(140,80,25,.45) 0, rgba(140,80,25,0) 110px),
      radial-gradient(circle at 380px 20px, rgba(150,100,40,.5) 0, rgba(150,100,40,0) 60px),
      radial-gradient(ellipse at 200px 380px, var(--dark-2) 0, var(--dark-1) 75%);
  }
  .brand-name{position:absolute;left:0;width:404px;top:290px;text-align:center;
    font-family:"Barlow Condensed",sans-serif;font-weight:600;color:var(--gold-light);
    font-size:34px;line-height:1.1;letter-spacing:2px}
  .brand-name .mark{display:block;width:14px;height:14px;border-radius:50%;background:var(--gold-light);margin:0 auto 12px}
  .brand-rule{position:absolute;top:654px;left:129px;width:158px;height:1px}
  .contact{position:absolute;left:0;width:404px;top:694px;text-align:center;
    font-family:"Barlow Condensed",sans-serif;font-size:16px;color:var(--gold-light);list-style:none}
  .contact li{display:flex;justify-content:center;align-items:center;gap:7px;height:28.5px}
  .contact svg{flex:none}

  /* menu side */
  .menu-title{position:absolute;left:596px;width:400px;top:52px;text-align:center;
    font-family:"Great Vibes",cursive;font-size:56px;color:var(--gold);line-height:1}
  .menu-title::before,.menu-title::after{content:"";display:inline-block;width:5px;height:5px;background:var(--gold);transform:rotate(45deg);vertical-align:middle;margin:0 22px}
  .section-tag{position:absolute;height:40px;background:var(--gold);color:#fff;
    font-family:"Barlow Condensed",sans-serif;font-weight:600;font-size:19px;line-height:40px;padding-left:17px}
  .section-tag.main{left:455px;top:161px;width:140px;clip-path:polygon(0 0,100% 0,96% 50%,100% 100%,0 100%)}
  .section-tag.side{left:853px;top:161px;width:140px;clip-path:polygon(0 0,100% 0,96% 50%,100% 100%,0 100%)}
  .section-tag.drinks{left:684px;top:633px;width:224px;padding:0;text-align:center;
    clip-path:polygon(0 0,100% 0,97% 50%,100% 100%,0 100%,3% 50%)}
  .column-divider{position:absolute;left:795px;top:225px;width:2px;height:365px;background:var(--gold)}

  .dish-list{position:absolute;width:300px;list-style:none}
  .dish-list.main{left:455px;top:224px}
  .dish-list.side{left:853px;top:224px}
  .dish-list.drinks-a{left:455px;top:710px}
  .dish-list.drinks-b{left:853px;top:710px}
  .dish{position:relative;height:100px}
  .dish-name{font-size:18px;font-weight:400;letter-spacing:.3px;line-height:24px;color:var(--ink)}
  .dish-name .initial{font-family:"Great Vibes",cursive;font-size:27px;line-height:1}
  .dish-desc{margin-top:4px;width:250px;font-size:12px;line-height:15.5px;color:var(--muted)}
  .dish-price{position:absolute;left:261px;top:28px;color:var(--gold);font-weight:500;font-size:29px;line-height:1}
  .dish-price small{font-size:15px;vertical-align:top;position:relative;top:-1px}
</style>
</head>
<body>
<main class="menu-sheet">
  <aside class="brand-panel" role="img" aria-label="Dark brown and amber background with soft glowing light spots">
    <h1 class="brand-name"><span class="mark"></span>GASTSTÄTTE<br>ZUM MÜHLSTEG</h1>
    <svg class="brand-rule" width="158" height="8" viewBox="0 0 158 8" style="top:650px;height:8px">
      <line x1="0" y1="4" x2="70" y2="4" stroke="#8a5a2a" stroke-width="1"/>
      <rect x="75" y="1.5" width="5" height="5" transform="rotate(45 77.5 4)" fill="none" stroke="#b07a3a" stroke-width="1"/>
      <line x1="88" y1="4" x2="158" y2="4" stroke="#8a5a2a" stroke-width="1"/>
    </svg>
    <ul class="contact">
      <li><svg width="11" height="14" viewBox="0 0 11 14"><path d="M5.5 0A5.5 5.5 0 0 0 0 5.5C0 9.5 5.5 14 5.5 14S11 9.5 11 5.5A5.5 5.5 0 0 0 5.5 0Zm0 7.6a2.1 2.1 0 1 1 0-4.2 2.1 2.1 0 0 1 0 4.2Z" fill="#fff"/></svg>Lindenweg 7, 34590 Wabern (Schwalm)</li>
      <li><svg width="14" height="14" viewBox="0 0 14 14"><circle cx="7" cy="7" r="7" fill="#fff"/><path d="M4.4 3.3l1.4 1.6-.7 1a5 5 0 0 0 3 3l1-.7 1.6 1.4-.9 1.1C6.8 10.9 3.1 7.2 3.3 4.2Z" fill="#3a0d04"/></svg>Frau Lena Brandt 152 80147263</li>
      <li><svg width="14" height="14" viewBox="0 0 14 14"><circle cx="7" cy="7" r="7" fill="#fff"/></svg>/ZumMuehlstegWabern</li>
    </ul>
  </aside>

  <h2 class="menu-title">Menu</h2>

  <div class="section-tag main">MAIN DISHES</div>
  <div class="section-tag side">SIDE DISHES</div>
  <div class="column-divider"></div>

  <ul class="dish-list main">
    <li class="dish"><h3 class="dish-name"><span class="initial">S</span>INT OCCAECAT</h3><p class="dish-desc">Sed ut perspiciatis unde omnis iste natus error sit voluptatem accusantium..........................</p><span class="dish-price"><small>€</small>5</span></li>
    <li class="dish"><h3 class="dish-name"><span class="initial">Q</span>UIS NOSTRUD</h3><p class="dish-desc">Sed ut perspiciatis unde omnis iste natus error sit voluptatem accusantium..........................</p><span class="dish-price"><small>€</small>7</span></li>
    <li class="dish"><h3 class="dish-name"><span class="initial">E</span>USMOD TEMPOR</h3><p class="dish-desc">Sed ut perspiciatis unde omnis iste natus error sit voluptatem accusantium..........................</p><span class="dish-price"><small>€</small>8</span></li>
    <li class="dish"><h3 class="dish-name"><span class="initial">L</span>OREM IPSUM</h3><p class="dish-desc">Sed ut perspiciatis unde omnis iste natus error sit voluptatem accusantium..........................</p><span class="dish-price"><small>€</small>3</span></li>
  </ul>

  <ul class="dish-list side">
    <li class="dish"><h3 class="dish-name"><span class="initial">S</span>INT OCCAECAT</h3><p class="dish-desc">Sed ut perspiciatis unde omnis iste natus error sit voluptatem accusantium..........................</p><span class="dish-price"><small>€</small>5</span></li>
    <li class="dish"><h3 class="dish-name"><span class="initial">Q</span>UIS NOSTRUD</h3><p class="dish-desc">Sed ut perspiciatis unde omnis iste natus error sit voluptatem accusantium..........................</p><span class="dish-price"><small>€</small>7</span></li>
    <li class="dish"><h3 class="dish-name"><span class="initial">E</span>USMOD TEMPOR</h3><p class="dish-desc">Sed ut perspiciatis unde omnis iste natus error sit voluptatem accusantium..........................</p><span class="dish-price"><small>€</small>8</span></li>
    <li class="dish"><h3 class="dish-name"><span class="initial">L</span>OREM IPSUM</h3><p class="dish-desc">Sed ut perspiciatis unde omnis iste natus error sit voluptatem accusantium..........................</p><span class="dish-price"><small>€</small>3</span></li>
  </ul>

  <div class="section-tag drinks">DRINKS</div>

  <ul class="dish-list drinks-a">
    <li class="dish"><h3 class="dish-name"><span class="initial">S</span>INT OCCAECAT</h3><p class="dish-desc">Sed ut perspiciatis unde omnis iste natus error sit voluptatem accusantium..........................</p><span class="dish-price"><small>€</small>5</span></li>
  </ul>
  <ul class="dish-list drinks-b">
    <li class="dish"><h3 class="dish-name"><span class="initial">S</span>INT OCCAECAT</h3><p class="dish-desc">Sed ut perspiciatis unde omnis iste natus error sit voluptatem accusantium..........................</p><span class="dish-price"><small>€</small>5</span></li>
  </ul>
</main>
</body>
</html>
```